Bargo Finch

I want a design for a website where users can insert products URLs from different sites and the user will get notified by email when that product's price changes.

On the homepage I'd like a big input where the user can insert a product's URL. On the same page the following will appear:
- my products that I follow (options: share, buy, unfollow) + it's current price and deviation from last time it's price has changed (I may have many products that I follow, so maybe a table layout would be wise. - just a suggestion)
- products that other people follow (options: follow). If my Chatterloop friends follow a certain product, I can see their photo(eg: friend1, friend2 and 5 others are following this product) (also, may people may follow a product.)

On the login page I can register using user / pass or using Chatterloop

The 3rd page is the product's page. Once I click on any product I go to this page. On this page I can see:
- picture, name and price and no of people following this product
- a chart with the product's price over the last 30 days
- list with friends that follow this product (when logged in)
- product options: follow / unfollow, share, buy

Then I want the design for an email template that I send when 1 or more prices of a user's products change.

Nice to have: want level for product - describes how much wanted is a product after a certain internal algorithm

NB:
- flat design (not really kestra, something more like the new Vyra interface - just a suggestion)
- I'd prefer a red theme (based on the idea that the site will be represented by a rooster)
- don't forget the design for basic elements: loading screen, popup, alert, messages, etc

I've posted an initial prototype with what I'd like the design to contain.

• - flat design
- must be simple. much white space
• as few gradients as possible

```html
<!DOCTYPE html>
<html lang="en">
<head>
<meta charset="utf-8">
<title>Bargo Finch – Price Tracker</title>
<link rel="stylesheet" href="https://fonts.googleapis.com/css2?family=Source+Sans+3:wght@400;600;700&display=swap">
<style>
:root{
  --page:#e4e4e4;
  --panel:#f9f9f9;
  --white:#ffffff;
  --ink:#1c1c1c;
  --dark:#262626;
  --red:#e0192f;
  --grey:#9a9a9a;
  --grey-light:#b0b0b0;
  --rule:#c9c9c9;
}
*{box-sizing:border-box;margin:0;padding:0}
html,body{width:924px;height:1200px;overflow:hidden}
body{background:var(--page);font-family:"Source Sans 3",Arial,sans-serif;color:var(--ink);position:relative}
.abs{position:absolute}

/* header */
.site-header{left:66px;top:21px;width:793px;height:45px;background:var(--white)}
.brand{left:0;top:0;width:126px;height:45px;background:var(--dark);color:var(--white);font-weight:700;font-size:13px;display:flex;align-items:center;justify-content:center;letter-spacing:.2px}
.nav-link{top:0;height:45px;line-height:45px;font-size:11.5px;font-weight:700;text-transform:uppercase}
.nav-divider{top:13px;width:1px;height:20px;background:#dcdcdc}
.user-avatar{left:649px;top:0;width:36px;height:45px;background:linear-gradient(#cfc6bd,#6f5d52)}
.user-toggle{left:685px;top:0;width:10px;height:45px;background:var(--dark)}
.user-toggle:after{content:"";position:absolute;left:2px;top:20px;border:3px solid transparent;border-top-color:#fff}
.user-name{left:719px;top:0;line-height:45px;font-size:11.5px;font-weight:700}

/* url input */
.url-form{left:170px;top:107px;width:584px;height:54px;background:var(--white)}
.url-placeholder{left:16px;top:0;line-height:54px;font-size:11px;font-style:italic;color:#c4c4c4}
.url-submit{right:0;top:0;width:54px;height:54px;background:var(--red)}

/* followed slider */
.my-product{left:66px;top:202px;width:793px;height:220px;background:var(--panel)}
.my-product-photo{left:0;top:0;width:366px;height:220px;background:linear-gradient(135deg,#5a5a5f,#1b1b1e 70%)}
.my-product-title{left:381px;top:12px;font-size:21px}
.my-product-desc{left:381px;top:58px;width:300px;font-size:11.5px;line-height:15px}
.price-box{left:711px;width:82px;height:65px;color:#fff;font-size:17px;line-height:15px;display:flex;flex-direction:column;align-items:center;justify-content:center}
.price-now{top:0;background:var(--dark)}
.price-change{top:73px;background:var(--red)}
.action-btn{top:179px;width:81px;height:24px;background:var(--dark);color:#fff;font-size:12px;line-height:24px;text-align:center}
.dot{top:447px;width:11px;height:11px;border-radius:50%}

/* others */
.section-title{left:65px;top:480px;font-size:27px;color:var(--grey);letter-spacing:.3px}
.card{width:256px;height:173px;background:var(--panel)}
.card-title{position:absolute;left:7px;top:0;line-height:24px;font-size:13.5px;white-space:nowrap}
.card-photo{position:absolute;left:0;top:24px;width:256px;height:110px}
.followers{position:absolute;left:7px;top:141px;display:flex;gap:3px}
.face{width:24px;height:24px}
.more{width:24px;height:24px;background:var(--dark);color:#fff;font-size:11px;line-height:24px;text-align:center}

/* footer */
.footer-rule{left:0;top:940px;width:924px;height:1px;background:var(--rule)}
.foot-head{top:963px;font-size:13px;color:var(--grey)}
.foot-text{font-size:11.5px;line-height:13.8px;color:var(--grey-light)}
.foot-list{list-style:none;font-size:11.5px;line-height:21px;color:var(--grey-light)}
.social{width:44px;height:40px;border-radius:3px;display:flex;align-items:center;justify-content:center;font-size:8px;font-weight:600;color:#fff;overflow:hidden;white-space:nowrap}
.social-long{font-size:7px;letter-spacing:-.1px}
.foot-brand{left:705px;top:1122px;width:142px;text-align:right;font-size:18px;font-weight:700;color:var(--grey)}
.copyright{left:68px;top:1138px;font-size:11px;color:var(--grey)}
</style>
</head>
<body>

<header class="abs site-header">
  <div class="abs brand">BARGO FINCH</div>
  <a class="abs nav-link" style="left:176px">Home</a>
  <span class="abs nav-divider" style="left:254px"></span>
  <a class="abs nav-link" style="left:285px">Products</a>
  <span class="abs nav-divider" style="left:374px"></span>
  <a class="abs nav-link" style="left:408px">Contact</a>
  <div class="abs user-avatar" role="img" aria-label="User profile photo"></div>
  <div class="abs user-toggle"></div>
  <div class="abs user-name">MILO VARGA</div>
</header>

<form class="abs url-form">
  <span class="abs url-placeholder">Insert Product URL</span>
  <div class="abs url-submit">
    <svg width="54" height="54" viewBox="0 0 54 54"><path d="M22 18 L33 27 L22 36 Z" fill="#fff"/></svg>
  </div>
</form>

<section class="abs my-product">
  <div class="abs my-product-photo" role="img" aria-label="Product photo: wristwatch with leather strap on dark background"></div>
  <h2 class="abs my-product-title" style="font-weight:400">Colorful Photography</h2>
  <p class="abs my-product-desc">Our true talent is storytelling. But, we make full use of every available method of distribution, new mediums, new formats, unique experiences and opportunities.</p>
  <div class="abs price-box price-now"><span>450</span><span>USD</span></div>
  <div class="abs price-box price-change"><span>+4</span><span>USD</span></div>
  <div class="abs action-btn" style="left:381px">Share</div>
  <div class="abs action-btn" style="left:471px">Buy</div>
  <div class="abs action-btn" style="left:560px">Unfollow</div>
</section>
<span class="abs dot" style="left:447px;background:var(--red)"></span>
<span class="abs dot" style="left:467px;background:#a9a9a9"></span>

<h2 class="abs section-title" style="font-weight:400">FOLLOWED BY OTHERS</h2>

<article class="abs card" style="left:66px;top:538px">
  <div class="card-title">Vireo Motion Dance 3 Bundle...</div>
  <div class="card-photo" role="img" aria-label="Game console bundle with controllers" style="background:linear-gradient(90deg,#222 0%,#555 45%,#1a4f6b 75%,#2a8fb5)"></div>
  <div class="followers"><span class="face" role="img" aria-label="Friend" style="background:#7e7a55"></span><span class="face" role="img" aria-label="Friend" style="background:#5c4a42"></span><span class="face" role="img" aria-label="Friend" style="background:#6a635c"></span><span class="more">+5</span></div>
</article>
<article class="abs card" style="left:334px;top:538px">
  <div class="card-title">Lumacast Digital HD Media...</div>
  <div class="card-photo" role="img" aria-label="Media streaming stick" style="background:linear-gradient(180deg,#c9866a,#efe6e0 45%,#2f3136 75%,#b9a79c)"></div>
  <div class="followers"><span class="face" role="img" aria-label="Friend" style="background:#7e7a55"></span><span class="face" role="img" aria-label="Friend" style="background:#5c4a42"></span><span class="face" role="img" aria-label="Friend" style="background:#6a635c"></span><span class="more">+5</span></div>
</article>
<article class="abs card" style="left:602px;top:538px">
  <div class="card-title">Diamond Engagement Ring 14K</div>
  <div class="card-photo" role="img" aria-label="Diamond ring on red fabric" style="background:radial-gradient(circle at 55% 45%,#e9e3e3 0,#c8141c 22%,#7a0a0e 100%)"></div>
  <div class="followers"><span class="face" role="img" aria-label="Friend" style="background:#4d3b46"></span><span class="face" role="img" aria-label="Friend" style="background:#b09a86"></span><span class="face" role="img" aria-label="Friend" style="background:#4b3428"></span><span class="more">+10</span></div>
</article>

<article class="abs card" style="left:66px;top:727px">
  <div class="card-title">Korean Fashion Bags - For Women</div>
  <div class="card-photo" role="img" aria-label="Brown leather handbag" style="background:radial-gradient(ellipse at 45% 55%,#8a4a22 0,#6b3417 35%,#d8d4d0 70%)"></div>
  <div class="followers"><span class="face" role="img" aria-label="Friend" style="background:#4d3b46"></span><span class="face" role="img" aria-label="Friend" style="background:#b09a86"></span><span class="face" role="img" aria-label="Friend" style="background:#4b3428"></span><span class="more">+5</span></div>
</article>
<article class="abs card" style="left:334px;top:727px">
  <div class="card-title">Mountaineering Boots (Men's 45)</div>
  <div class="card-photo" role="img" aria-label="Pair of grey mountaineering boots" style="background:linear-gradient(180deg,#8a8784,#555250 50%,#c9c6c2)"></div>
  <div class="followers"><span class="face" role="img" aria-label="Friend" style="background:#7e7a55"></span><span class="face" role="img" aria-label="Friend" style="background:#5c4a42"></span><span class="face" role="img" aria-label="Friend" style="background:#6a635c"></span><span class="more">+5</span></div>
</article>
<article class="abs card" style="left:602px;top:727px">
  <div class="card-title">Wedge Sandals with Ankle Straps</div>
  <div class="card-photo" role="img" aria-label="Black wedge sandal on white" style="background:radial-gradient(ellipse at 50% 55%,#2a2a2a 0,#5a5a5a 14%,#ffffff 32%)"></div>
  <div class="followers"><span class="face" role="img" aria-label="Friend" style="background:#4d3b46"></span><span class="face" role="img" aria-label="Friend" style="background:#b09a86"></span><span class="face" role="img" aria-label="Friend" style="background:#4b3428"></span><span class="more">+10</span></div>
</article>

<footer>
  <div class="abs footer-rule"></div>

  <h3 class="abs foot-head" style="left:70px;font-weight:400">About us</h3>
  <p class="abs foot-text" style="left:70px;top:995px;width:190px">Lorem ipsum dolor sit amet, consectetur adipiscing elit. Morbi euismod placerat dui et tincidunt. Sed sollicitudin posuere auctor. Phasellus at ultricies nisi. Integer at leo eros. Ut nec lorem id orci convallis porta. Donec pharetra neque eu velit dictum molestie.</p>

  <h3 class="abs foot-head" style="left:337px;font-weight:400">Explore</h3>
  <ul class="abs foot-list" style="left:337px;top:982px">
    <li>Home</li><li>About Us</li><li>Services</li><li>Feature</li><li>Blog</li>
  </ul>

  <h3 class="abs foot-head" style="left:521px;font-weight:400">Contact us</h3>
  <p class="abs foot-text" style="left:521px;top:992px">BargoFinch.com<br>Lantern Street 48<br>Q7 - 310 - Nordvale</p>
  <p class="abs foot-text" style="left:521px;top:1047px">Phone: 555-0142-210<br>Fax: 555-0142-211</p>

  <h3 class="abs foot-head" style="left:705px;font-weight:400">Connect with us</h3>
  <div class="abs social" style="left:706px;top:991px;background:#d42121">Vidlo</div>
  <div class="abs social" style="left:760px;top:991px;background:#7cc2dc">Linkora</div>
  <div class="abs social" style="left:815px;top:991px;background:#fff;border:2px solid #b8b8b8;color:#555">Snapdot</div>
  <div class="abs social" style="left:706px;top:1041px;background:#c9302c">Plusio</div>
  <div class="abs social social-long" style="left:760px;top:1041px;background:#4a6fb5">Chatterloop</div>
  <div class="abs social" style="left:815px;top:1041px;background:#33b4e8">Chirpa</div>

  <div class="abs foot-brand">BARGO FINCH</div>
  <p class="abs copyright">© Copyright 2013 - BargoFinch.com. All rights reserved.</p>
</footer>

</body>
</html>
```